Free Online Jumpstart Invitation Card

Creating a business card template for our team members that are offering a free 4-day online course to teach people healthy habits that will allow them to start losing weight. The key part of the promotion is that the program is free. This card will be giving out to people on a daily basis and needs to capture people's attention. To do so, I would like to use a collage of before and after photos. The final design should create curiosity in trying our online program since it is free and can be their chance to transform their health and body.

Target Market(s)

Busy men and women looking for a solution to transforming their body in regards to their weight, body shape, or energy and health.

Industry/Entity Type

Health And Wellness

Contact Information for Business Card

Coach (Name of Person)
Whatsapp Number:
Instagram Name:
Facebook Page:

Requirements
Must have
• some before and after photos
Nice to have
• catchy slogan
• area for Whatsapp QR Code

```html
<!DOCTYPE html>
<html lang="en">
<head>
<meta charset="utf-8">
<title>Free Online Jumpstart Invitation Card</title>
<link href="https://fonts.googleapis.com/css2?family=Oswald:wght@500;600&family=Open+Sans:ital,wght@1,400&display=swap" rel="stylesheet">
<style>
  :root {
    --page-bg: #3a3a3c;
    --card-deep: #0b1724;
    --card-glow: #143a55;
    --brand-green: #6db446;
    --text-white: #f4f6f8;
    --photo-dark: #1b1a1c;
    --photo-warm: #7a5a48;
    --photo-light: #cfc7bf;
  }
  * { box-sizing: border-box; margin: 0; padding: 0; }
  html, body {
    width: 1200px; height: 1200px; overflow: hidden;
    background: var(--page-bg);
  }
  .canvas {
    width: 1200px; height: 1200px;
    display: flex; align-items: center; justify-content: center;
  }
  .card {
    position: relative;
    width: 1050px; height: 600px;
    border-radius: 4px;
    background: radial-gradient(ellipse at 52% 58%, var(--card-glow) 0%, #0f2638 38%, var(--card-deep) 78%);
    overflow: hidden;
  }
  .slogan {
    position: absolute; left: 0; right: 0; top: 150px;
    text-align: center;
    font-family: "Oswald", sans-serif; font-weight: 600;
    font-size: 118px; line-height: 1; letter-spacing: 1px;
    color: var(--brand-green);
    text-transform: uppercase;
  }
  .section-title {
    position: absolute; left: 0; right: 0; top: 318px;
    text-align: center;
    font-family: "Oswald", sans-serif; font-weight: 500;
    font-size: 50px; line-height: 1;
    color: var(--text-white);
    text-transform: uppercase;
  }
  .results-strip {
    position: absolute; left: 28px; right: 28px; top: 405px; height: 150px;
    border-radius: 8px; overflow: hidden;
    border: 2px solid var(--brand-green);
    display: flex;
  }
  .result {
    flex: 1; display: flex; flex-direction: column;
  }
  .result-photo { flex: 1; }
  .result-photo.before { background: linear-gradient(180deg, var(--photo-light), var(--photo-warm)); }
  .result-photo.after { background: linear-gradient(180deg, var(--photo-dark), #4a3a34 70%, var(--photo-dark)); }
  .result-label {
    height: 30px; background: var(--brand-green);
    font-family: "Open Sans", sans-serif; font-style: italic;
    font-size: 16px; line-height: 30px; text-align: center;
    color: var(--text-white);
  }
</style>
</head>
<body>
<div class="canvas">
  <section class="card">
    <h1 class="slogan">Your Slogan Here</h1>
    <h2 class="section-title">Our Customers</h2>
    <div class="results-strip">
      <div class="result"><div class="result-photo before" role="img" aria-label="Customer photo before the program"></div><div class="result-label">Before</div></div>
      <div class="result"><div class="result-photo after" role="img" aria-label="Customer photo after the program"></div><div class="result-label">After</div></div>
      <div class="result"><div class="result-photo before" role="img" aria-label="Customer photo before the program"></div><div class="result-label">Before</div></div>
      <div class="result"><div class="result-photo after" role="img" aria-label="Customer photo after the program"></div><div class="result-label">After</div></div>
      <div class="result"><div class="result-photo before" role="img" aria-label="Customer photo before the program"></div><div class="result-label">Before</div></div>
      <div class="result"><div class="result-photo after" role="img" aria-label="Customer photo after the program"></div><div class="result-label">After</div></div>
      <div class="result"><div class="result-photo before" role="img" aria-label="Customer photo before the program"></div><div class="result-label">Before</div></div>
      <div class="result"><div class="result-photo after" role="img" aria-label="Customer photo after the program"></div><div class="result-label">After</div></div>
      <div class="result"><div class="result-photo before" role="img" aria-label="Customer photo before the program"></div><div class="result-label">Before</div></div>
      <div class="result"><div class="result-photo after" role="img" aria-label="Customer photo after the program"></div><div class="result-label">After</div></div>
      <div class="result"><div class="result-photo before" role="img" aria-label="Customer photo before the program"></div><div class="result-label">Before</div></div>
      <div class="result"><div class="result-photo after" role="img" aria-label="Customer photo after the program"></div><div class="result-label">After</div></div>
    </div>
  </section>
</div>
</body>
</html>
```